I need 8 Banners for my Web Site

I am building an online store with prestashop, The store will sell costa rican coffee bags, I have the site almost ready, but I need some nice banners.

Top Banners
3 Banners
940x446

2 Banner
218x158

Footer Banners
3 Banners
280x100

Please see the attached images to see how they will fit in the web page.
Also you can see some of the products and images over here https://www.faceplaza-social.net/TheAmberCrate

All I need is that the banners fit with the website design, and that they look "coffee related",(think about a coffee shop with fine coffee products, fresh coffee from a latin american country, think about a mountain full of coffee plants, think about nature, think about flavor)

Colors are brown,green, gray, white, but if you see something else can match those colors feel free to use them.

Also Below the texts you must Use:

3 Banners
940x446

#1
Welcome Coffee Lovers!
The Amber Crate Store is Open Now!

#2
Fresh Coffee from the Costa Rican Mountains!
Get your coffee Now!

#3
Free Coffee Samples!
Fill our form and participate for weekly promotions!

2 Banners
218x158

#1
Carbon Neutral Coffee
Get it Now!

#2
Coffee from the TarrazĂș Mountains
Buy Now!

3 Banners
280x100

#1
Coffee from Velmira Estate Farm
Shop Now!

#2
Lurano Coffee, the finest beans to your door!
Shop Now!

#3
Check our Espresso catalog!
Shop Now!

```html
<!DOCTYPE html>
<html lang="en">
<head>
<meta charset="utf-8">
<title>Free Coffee Samples – The Amber Crate Store</title>
<link rel="stylesheet" href="https://fonts.googleapis.com/css2?family=Great+Vibes&family=Shadows+Into+Light&display=swap">
<style>
  :root {
    --espresso: #3a2212;
    --roast-dark: #2a170b;
    --caramel: #a4561e;
    --caramel-deep: #7d3c12;
    --gold: #d9ab52;
    --gold-soft: #b9823a;
    --wood: #5b3a21;
    --wood-light: #8a5a33;
    --hair: #4a2a14;
    --skin: #d9a878;
    --linen: #cdb38a;
    --cream: #ffffff;
  }
  html, body {
    margin: 0;
    padding: 0;
    width: 1200px;
    height: 569px;
    overflow: hidden;
    background: var(--roast-dark);
  }
  .banner {
    position: relative;
    width: 1200px;
    height: 569px;
    overflow: hidden;
  }
  .banner__backdrop {
    position: absolute;
    inset: 0;
    background:
      radial-gradient(ellipse 420px 300px at 760px 190px, rgba(240, 200, 110, 0.85), rgba(240, 200, 110, 0) 70%),
      linear-gradient(100deg, var(--roast-dark) 0%, var(--gold-soft) 40%, var(--gold) 62%, var(--espresso) 100%);
  }
  .banner__portrait {
    position: absolute;
    left: 0;
    top: 0;
    width: 440px;
    height: 569px;
    background:
      radial-gradient(ellipse 130px 170px at 200px 170px, var(--skin), rgba(217, 168, 120, 0) 100%),
      radial-gradient(ellipse 150px 110px at 210px 420px, var(--linen), rgba(205, 179, 138, 0) 100%),
      linear-gradient(90deg, var(--hair) 0%, #7a4a24 35%, #8e5d30 60%, rgba(142, 93, 48, 0) 100%);
  }
  .banner__table {
    position: absolute;
    left: 540px;
    top: 380px;
    width: 660px;
    height: 189px;
    background:
      radial-gradient(ellipse 160px 70px at 560px 120px, rgba(230, 200, 150, 0.55), rgba(230, 200, 150, 0) 100%),
      linear-gradient(180deg, rgba(91, 58, 33, 0) 0%, var(--wood-light) 45%, var(--wood) 100%);
  }
  .banner__headline {
    position: absolute;
    left: 366px;
    top: 32px;
    width: 834px;
    height: 195px;
    background: var(--espresso);
    display: flex;
    align-items: center;
    justify-content: center;
    box-shadow: 0 4px 14px rgba(0,0,0,0.35);
  }
  .banner__title {
    margin: 0;
    font-family: "Great Vibes", cursive;
    font-weight: 400;
    font-size: 98px;
    line-height: 1;
    color: var(--cream);
    padding-right: 40px;
  }
  .banner__strip {
    position: absolute;
    background: linear-gradient(90deg, rgba(164, 86, 30, 0.92), rgba(125, 60, 18, 0.88));
    box-shadow: 0 3px 10px rgba(0,0,0,0.3);
  }
  .banner__strip--upper {
    left: 439px;
    top: 259px;
    width: 761px;
    height: 102px;
  }
  .banner__strip--lower {
    left: 647px;
    top: 374px;
    width: 553px;
    height: 98px;
  }
  .banner__tagline {
    position: absolute;
    margin: 0;
    font-family: "Shadows Into Light", cursive;
    font-size: 62px;
    line-height: 1;
    color: var(--cream);
    white-space: nowrap;
    transform: skewX(-8deg);
  }
  .banner__tagline--upper {
    left: 472px;
    top: 274px;
  }
  .banner__tagline--lower {
    left: 694px;
    top: 388px;
  }
</style>
</head>
<body>
  <section class="banner">
    <div class="banner__backdrop"></div>
    <div class="banner__portrait" role="img" aria-label="Woman with closed eyes and long brown hair holding a steaming white cup of coffee"></div>
    <div class="banner__table" role="img" aria-label="Wooden table with scattered coffee beans and a saucer"></div>

    <div class="banner__headline">
      <h1 class="banner__title">Free Coffee Samples!</h1>
    </div>

    <div class="banner__strip banner__strip--upper"></div>
    <div class="banner__strip banner__strip--lower"></div>

    <p class="banner__tagline banner__tagline--upper">Fill our form and participate</p>
    <p class="banner__tagline banner__tagline--lower">for weekly promotions!</p>
  </section>
</body>
</html>
```